Northfield Server Crate requires an Email Marketing Design template

Northfield Server Crate are a rapidly expanding UK based internet hosting company that have just re-branded through Craft Lantern.
We provide internet based services such as website hosting, dedicated and managed servers, domain names as well as email solutions to name a few. We pride ourselves on being able to provide a comprehensive, secure, future proofed and scalable platform for our clients to communicate and do business on.
Northfield Server Crate are looking to go live with a new website on 1st August. In preparation for this we would like to have an HTML Email Template designed for our launch!
We are also having a really big push on the reseller market allowing potential resellers and their end users to manage their own services via a consolidated portal with many features and functions that will grow over time.

Target Market(s)
We have 3 core target markets, the end user who would be the likes of web designers or developers. A reseller market who would want to resell our hosted services and the final target market would be a business client that would want high end server and hosting solutions.
Industry/Entity Type
Internet Service Provider
Requirements
Must have
- To ensure it is inline with the new brand (see attached files).

```html
<!DOCTYPE html>
<html lang="en">
<head>
<meta charset="utf-8">
<title>Northfield Server Crate — Launch Email</title>
<link rel="stylesheet" href="https://fonts.googleapis.com/css2?family=Open+Sans:wght@400;600;700;800&family=Archivo+Black&display=swap">
<style>
:root{
  --teal:#1cb3b3;
  --teal-light:#6fe0dc;
  --teal-dark:#128c8f;
  --navy:#1b2430;
  --grey:#8b9197;
  --grey-light:#e9ecee;
  --hero-bg:#f1f4f6;
  --text:#222a33;
  --muted:#555d66;
  --white:#ffffff;
}
*{box-sizing:border-box;margin:0;padding:0}
html,body{width:1200px;height:2212px;overflow:hidden;background:var(--white)}
body{position:relative;font-family:"Open Sans",Arial,sans-serif;color:var(--text)}

/* Header */
.site-header{position:absolute;left:0;top:0;width:1200px;height:120px;background:var(--white)}
.header-bar{position:absolute;left:0;top:0;width:1200px;height:120px}
.brand{position:absolute;left:40px;top:22px;display:flex;align-items:center;gap:18px}
.brand-mark{width:76px;height:76px;border-radius:50%;background:var(--teal)}
.brand-name{font-weight:800;font-size:30px;line-height:34px;color:var(--navy);width:260px}
.call-us{position:absolute;left:520px;top:40px;color:var(--white);font-weight:700;font-size:24px;display:flex;align-items:center;gap:14px}
.login-btn{position:absolute;left:1030px;top:36px;width:140px;height:50px;background:var(--white);color:var(--teal-dark);font-weight:700;font-size:22px;display:flex;align-items:center;justify-content:center;border-radius:4px}

/* Hero */
.hero{position:absolute;left:0;top:120px;width:1200px;height:540px;overflow:hidden;background:var(--hero-bg)}
.hero-photo{position:absolute;left:560px;top:0;width:640px;height:540px;background:linear-gradient(160deg,#f6f8f9 0%,#d9dfe4 35%,#a9b3bc 65%,#e6ebee 100%)}
.hero-badge{position:absolute;left:110px;top:130px;width:300px;height:300px;border-radius:24px;background:linear-gradient(160deg,#24303d,var(--navy));border:6px solid var(--teal)}
.badge-text{position:absolute;left:110px;top:130px;width:300px;height:300px;display:flex;flex-direction:column;align-items:center;justify-content:center;gap:6px;color:var(--white)}
.badge-text .only,.badge-text .per{font-weight:800;font-size:28px;letter-spacing:1px;color:var(--teal-light)}
.badge-text .amount{font-family:"Archivo Black",Arial,sans-serif;font-size:96px;line-height:104px;color:var(--teal)}
.hero-title{position:absolute;left:470px;top:250px;font-weight:800;font-size:36px;color:var(--navy);letter-spacing:.5px}
.hero-title span{color:var(--teal)}

/* Domain search band */
.domain-band{position:absolute;left:0;top:660px;width:1200px;height:84px;background:linear-gradient(90deg,var(--teal-light),var(--teal) 50%,var(--teal-light));display:flex;align-items:center;justify-content:center;font-family:"Archivo Black",Arial,sans-serif;font-size:44px;letter-spacing:6px;color:var(--navy)}

/* Section titles */
.section-title{position:absolute;left:0;width:1200px;text-align:center;font-weight:700;font-size:36px;color:var(--text)}
.section-rule{position:absolute;left:100px;width:1000px;height:2px;background:var(--grey-light)}
.section-rule::after{content:"";position:absolute;left:470px;top:-2px;width:60px;height:6px;background:var(--teal)}

/* Service cards */
.services{position:absolute;left:100px;top:900px;width:1020px;height:400px;display:flex;gap:20px}
.service-card{position:relative;width:240px;height:380px;background:var(--white);border-top:6px solid var(--teal);box-shadow:0 2px 10px rgba(0,0,0,.15);text-align:center;padding-top:86px}
.service-icon{position:absolute;left:75px;top:-50px;width:90px;height:90px;border-radius:50%;background:var(--grey);border:6px solid var(--white);box-shadow:0 0 0 3px var(--grey-light);display:flex;align-items:center;justify-content:center}
.service-card h3{font-size:19px;font-weight:700;text-transform:uppercase;margin-bottom:12px}
.service-card p{font-size:17px;line-height:24px;color:var(--muted);padding:0 18px}
.price{margin-top:18px;font-size:38px;font-weight:700;color:var(--text)}
.price small{font-size:16px;font-weight:400;color:var(--muted)}
.card-btn{position:absolute;left:30px;bottom:24px;width:180px;height:46px;background:var(--grey);color:var(--navy);font-weight:600;font-size:18px;display:flex;align-items:center;justify-content:center}
.card-btn.primary{background:var(--navy);color:var(--white)}

/* Features */
.features{position:absolute;left:80px;top:1440px;width:1040px;display:flex;justify-content:space-between}
.feature{width:190px;text-align:center}
.feature-icon{width:116px;height:116px;margin:0 auto 18px;border-radius:50%;background:var(--teal);border:6px solid var(--white);box-shadow:0 0 0 4px var(--teal-light);display:flex;align-items:center;justify-content:center}
.feature span{font-weight:700;font-size:20px;line-height:26px}

/* Footer */
.footer{position:absolute;left:0;top:1700px;width:1200px;height:460px;overflow:hidden;background:var(--navy)}
.footer-shape{position:absolute;inset:0}
.footer-title{position:absolute;left:100px;top:44px;color:var(--white);font-weight:700;font-size:28px}
.contact-row{position:absolute;left:100px;display:flex;align-items:flex-start;gap:26px;color:#cfd5db;font-size:18px;line-height:27px}
.contact-icon{flex:none;width:48px;height:48px;border-radius:50%;background:var(--teal);display:flex;align-items:center;justify-content:center}
.social{position:absolute;left:800px;top:205px;display:flex;gap:30px}
.social i{display:block;width:70px;height:70px;border-radius:50%;border:3px solid var(--white);background:rgba(255,255,255,.12)}

/* Bottom bar */
.legal{position:absolute;left:0;top:2160px;width:1200px;height:52px;background:var(--grey-light);display:flex;align-items:center;justify-content:space-between;padding:0 100px;font-size:17px;color:var(--muted)}
.legal nav{display:flex;gap:16px}
</style>
</head>
<body>

<header class="site-header">
  <svg class="header-bar" width="1200" height="120" viewBox="0 0 1200 120">
    <polygon points="470,0 1200,0 1200,120 440,120" fill="var(--teal)"/>
  </svg>
  <div class="brand"><span class="brand-mark"></span><span class="brand-name">Northfield Server Crate</span></div>
  <div class="call-us">
    <svg width="28" height="28" viewBox="0 0 24 24"><path fill="#fff" d="M6.6 10.8a15 15 0 0 0 6.6 6.6l2.2-2.2c.3-.3.7-.4 1-.2 1.1.4 2.3.6 3.6.6.6 0 1 .4 1 1V20c0 .6-.4 1-1 1A17 17 0 0 1 3 4c0-.6.4-1 1-1h3.5c.6 0 1 .4 1 1 0 1.3.2 2.5.6 3.6.1.3 0 .7-.2 1z"/></svg>
    CALL US NOW : +1 800 5550 2714
  </div>
  <div class="login-btn">LOGIN</div>
</header>

<section class="hero">
  <div class="hero-photo" role="img" aria-label="Photo of a smiling woman in a grey top at a laptop holding a payment card"></div>
  <div class="hero-badge" role="img" aria-label="Decorative hexagonal price badge with ribbon banners"></div>
  <div class="badge-text">
    <span class="only">ONLY</span>
    <span class="amount">$99</span>
    <span class="per">PER MONTH</span>
  </div>
  <div class="hero-title">ADVANCED <span>WEB HOSTING</span></div>
</section>

<div class="domain-band">DOMAIN NAME SEARCH HERE!</div>

<h2 class="section-title" style="top:778px">Northfield Server Crate</h2>
<div class="section-rule" style="top:846px"></div>

<section class="services">
  <article class="service-card">
    <div class="service-icon"><svg width="48" height="48" viewBox="0 0 24 24"><path fill="#fff" d="M19 18H7a5 5 0 0 1-.6-10A6 6 0 0 1 18 9a4.5 4.5 0 0 1 1 9z"/></svg></div>
    <h3>Web Hosting</h3>
    <p>Fast, reliable &amp; secure cloud web hosting with UK support.</p>
    <div class="price">£49 <small>p/m</small></div>
    <div class="card-btn primary">Find Out More</div>
  </article>
  <article class="service-card">
    <div class="service-icon"><svg width="46" height="46" viewBox="0 0 24 24"><g fill="#fff"><rect x="4" y="3" width="16" height="5" rx="1"/><rect x="4" y="10" width="16" height="5" rx="1"/><rect x="4" y="17" width="16" height="4" rx="1"/></g></svg></div>
    <h3>Dedicated Server</h3>
    <p>Fast, reliable &amp; secure cloud web hosting with UK support.</p>
    <div class="price">£39 <small>p/m</small></div>
    <div class="card-btn">Find Out More</div>
  </article>
  <article class="service-card">
    <div class="service-icon"><svg width="48" height="48" viewBox="0 0 24 24" fill="none" stroke="#fff" stroke-width="2"><circle cx="12" cy="12" r="9"/><path d="M3 12h18M12 3c3 3 3 15 0 18M12 3c-3 3-3 15 0 18"/></svg></div>
    <h3>Domain Name</h3>
    <p>Fast, reliable &amp; secure cloud web hosting with UK support.</p>
    <div class="price">£29 <small>p/m</small></div>
    <div class="card-btn">Find Out More</div>
  </article>
  <article class="service-card">
    <div class="service-icon"><svg width="48" height="48" viewBox="0 0 24 24"><path fill="#fff" d="M10 3h4v7h4l-6 7-6-7h4zM3 18h18v3H3z"/></svg></div>
    <h3>VPS</h3>
    <p>Fast, reliable &amp; secure cloud web hosting with UK support.</p>
    <div class="price">£19 <small>p/m</small></div>
    <div class="card-btn">Find Out More</div>
  </article>
</section>

<div class="section-rule" style="top:1314px;height:1px"></div>
<h2 class="section-title" style="top:1326px">Northfield Server Crate</h2>
<div class="section-rule" style="top:1396px"></div>

<section class="features">
  <div class="feature">
    <div class="feature-icon"><svg width="56" height="56" viewBox="0 0 24 24" fill="none" stroke="#fff" stroke-width="2"><circle cx="12" cy="12" r="9"/><text x="12" y="15" text-anchor="middle" font-family="Open Sans, sans-serif" font-size="7" font-weight="700" fill="#fff" stroke="none">24</text></svg></div>
    <span>Free 24X7<br>Support</span>
  </div>
  <div class="feature">
    <div class="feature-icon"><svg width="56" height="56" viewBox="0 0 24 24"><path fill="#fff" d="M19 18H7a5 5 0 0 1-.6-10A6 6 0 0 1 18 9a4.5 4.5 0 0 1 1 9z"/><path fill="var(--teal)" d="M11 16v-4H9l3-3 3 3h-2v4z"/></svg></div>
    <span>Free<br>Migration</span>
  </div>
  <div class="feature">
    <div class="feature-icon"><svg width="56" height="56" viewBox="0 0 24 24" fill="none" stroke="#fff" stroke-width="2"><path d="M2 12s4-6 10-6 10 6 10 6-4 6-10 6S2 12 2 12z"/><circle cx="12" cy="12" r="3"/><path d="M4 20 20 4"/></svg></div>
    <span>No Hidden<br>Charges</span>
  </div>
  <div class="feature">
    <div class="feature-icon"><svg width="56" height="56" viewBox="0 0 24 24"><path fill="#fff" d="M12 3 2 12h3v8h5v-5h4v5h5v-8h3z"/></svg></div>
    <span>Great Value<br>Domain Names</span>
  </div>
  <div class="feature">
    <div class="feature-icon"><svg width="56" height="56" viewBox="0 0 24 24"><path fill="#fff" d="M12 21 3.5 12.5A5 5 0 0 1 12 6a5 5 0 0 1 8.5 6.5z"/></svg></div>
    <span>Our Customers<br>Love Us</span>
  </div>
</section>

<footer class="footer">
  <svg class="footer-shape" width="1200" height="460" viewBox="0 0 1200 460">
    <polygon points="800,0 1200,0 1200,460 620,460" fill="var(--teal)"/>
    <polygon points="790,0 800,0 620,460 610,460" fill="var(--white)"/>
  </svg>
  <div class="footer-title">Northfield Server Crate</div>
  <div class="contact-row" style="top:110px">
    <span class="contact-icon"><svg width="24" height="24" viewBox="0 0 24 24"><path fill="#fff" d="M12 2a7 7 0 0 0-7 7c0 5 7 13 7 13s7-8 7-13a7 7 0 0 0-7-7zm0 9.5A2.5 2.5 0 1 1 12 6.5a2.5 2.5 0 0 1 0 5z"/></svg></span>
    <div>Press and Communications Manager<br>Unit 4, Harbour Yard<br>7-9 Quay Lane<br>London SE9 4QT</div>
  </div>
  <div class="contact-row" style="top:262px;align-items:center">
    <span class="contact-icon"><svg width="24" height="24" viewBox="0 0 24 24"><path fill="#fff" d="M6.6 10.8a15 15 0 0 0 6.6 6.6l2.2-2.2c.3-.3.7-.4 1-.2 1.1.4 2.3.6 3.6.6.6 0 1 .4 1 1V20c0 .6-.4 1-1 1A17 17 0 0 1 3 4c0-.6.4-1 1-1h3.5c.6 0 1 .4 1 1 0 1.3.2 2.5.6 3.6.1.3 0 .7-.2 1z"/></svg></span>
    <div>+1 800 5550 2714</div>
  </div>
  <div class="contact-row" style="top:340px;align-items:center">
    <span class="contact-icon"><svg width="24" height="24" viewBox="0 0 24 24"><path fill="#fff" d="M3 5h18v14H3zm2 2v.5l7 5 7-5V7l-7 5z"/></svg></span>
    <div>info@northfieldcrate.com</div>
  </div>
  <div class="social"><i></i><i></i><i></i></div>
</footer>

<div class="legal">
  <span>Copyright 2015 Northfield Server Crate | All Rights Reserved.</span>
  <nav><span>Support</span><span>|</span><span>Privacy</span><span>|</span><span>Terms</span></nav>
</div>

</body>
</html>
```